Property developer, money partner needs business card design using logo concept provided

Our company develops residential properties, does money lends for joint ventures in property deals and finds property deals for other money partners. We have provided a basic logo for you to work from. Any graphic or logo design on the card is to communicate development and finance collaboration. Color choice is not so important for us, but color choice does need to reflect professionalism.

```html
<!DOCTYPE html>
<html lang="en">
<head>
<meta charset="utf-8">
<title>Brightfold Property Solutions – Business Card</title>
<link rel="stylesheet" href="https://fonts.googleapis.com/css2?family=Montserrat:wght@700&family=Open+Sans:wght@400;600;700&display=swap">
<style>
  :root {
    --stage: #3a3a3a;
    --card: #ffffff;
    --brand-blue: #0a6fbe;
    --deep-blue: #1d4f9c;
    --brand-red: #9b1b1e;
    --ink: #1e1e1e;
    --muted: #333333;
  }
  * { margin: 0; padding: 0; box-sizing: border-box; }
  html, body { width: 1200px; height: 689px; overflow: hidden; }
  body {
    background: var(--stage);
    font-family: "Open Sans", sans-serif;
    color: var(--ink);
    position: relative;
  }
  .card {
    position: absolute;
    top: 190px;
    width: 540px;
    height: 309px;
    background: var(--card);
    border-radius: 18px;
    overflow: hidden;
  }
  .card--front { left: 40px; }
  .card--back { left: 620px; }

  .brand {
    position: absolute;
    display: flex;
    flex-direction: column;
    align-items: center;
    text-align: center;
  }
  .brand__mark {
    width: 64px; height: 64px;
    border-radius: 50%;
    background: var(--brand-blue);
    margin-bottom: 12px;
  }
  .brand__name {
    font-family: "Montserrat", sans-serif;
    font-weight: 700;
    font-size: 24px;
    letter-spacing: 3px;
    color: var(--deep-blue);
  }
  .brand__tagline {
    font-size: 13px;
    letter-spacing: 2.5px;
    color: var(--ink);
    margin-top: 2px;
  }
  .brand__acn {
    font-size: 9px;
    letter-spacing: 2px;
    color: var(--ink);
    margin-top: 2px;
  }
  .card--front .brand { left: 0; right: 0; top: 78px; }
  .card--back .brand { left: 24px; width: 220px; top: 70px; }
  .card--back .brand__name { font-size: 20px; letter-spacing: 2px; }
  .card--back .brand__tagline { font-size: 11px; letter-spacing: 2px; }
  .card--back .brand__acn { font-size: 8px; }

  .divider {
    position: absolute;
    left: 262px; top: 38px;
    width: 1.5px; height: 150px;
    background: var(--brand-blue);
  }
  .contact {
    position: absolute;
    left: 284px; top: 30px;
  }
  .contact__name {
    font-weight: 700;
    font-size: 22px;
    color: var(--brand-blue);
    line-height: 1.1;
  }
  .contact__role {
    font-size: 12px;
    color: var(--muted);
    margin-bottom: 12px;
  }
  .contact__list { list-style: none; }
  .contact__item {
    display: flex;
    align-items: center;
    gap: 7px;
    font-size: 12px;
    line-height: 19px;
    color: var(--muted);
  }
  .contact__item svg { width: 11px; height: 11px; flex: none; fill: var(--brand-blue); }
  .contact__address {
    font-size: 12px;
    line-height: 17px;
    color: var(--muted);
    margin-top: 8px;
    padding-left: 18px;
  }
  .wave { position: absolute; left: 0; top: 0; width: 540px; height: 309px; }
</style>
</head>
<body>

<section class="card card--front" aria-label="Card front">
  <div class="brand">
    <span class="brand__mark"></span>
    <span class="brand__name">BRIGHTFOLD</span>
    <span class="brand__tagline">Property Solutions</span>
    <span class="brand__acn">A.C.N 418 903 276</span>
  </div>
</section>

<section class="card card--back" aria-label="Card back">
  <svg class="wave" viewBox="0 0 540 309" aria-hidden="true">
    <path d="M540 160 C470 190 410 245 330 272 C240 300 110 300 0 300 L0 309 L540 309 Z" fill="var(--brand-blue)"/>
    <path d="M540 152 C470 182 410 237 330 264 C240 292 110 292 0 292" fill="none" stroke="#ffffff" stroke-width="3"/>
    <path d="M540 142 C480 166 430 206 380 246" fill="none" stroke="var(--brand-red)" stroke-width="3"/>
  </svg>

  <div class="brand">
    <span class="brand__mark"></span>
    <span class="brand__name">BRIGHTFOLD</span>
    <span class="brand__tagline">Property Solutions</span>
    <span class="brand__acn">A.C.N 418 903 276</span>
  </div>

  <div class="divider"></div>

  <div class="contact">
    <p class="contact__name">Aaron Whitfield</p>
    <p class="contact__role">Managing Director</p>
    <ul class="contact__list">
      <li class="contact__item">
        <svg viewBox="0 0 24 24"><path d="M6.6 10.8a15 15 0 0 0 6.6 6.6l2.2-2.2c.3-.3.7-.4 1-.2 1.1.4 2.3.6 3.6.6.6 0 1 .4 1 1V20c0 .6-.4 1-1 1A17 17 0 0 1 3 4c0-.6.4-1 1-1h3.5c.6 0 1 .4 1 1 0 1.3.2 2.5.6 3.6.1.3 0 .7-.2 1z"/></svg>
        123 456 789
      </li>
      <li class="contact__item">
        <svg viewBox="0 0 24 24"><path d="M7 1h10a2 2 0 0 1 2 2v18a2 2 0 0 1-2 2H7a2 2 0 0 1-2-2V3a2 2 0 0 1 2-2zm0 3v14h10V4z"/></svg>
        123 456 789
      </li>
      <li class="contact__item">
        <svg viewBox="0 0 24 24"><path d="M2 5h20v14H2zm2 2v.5l8 5 8-5V7z"/></svg>
        info@yourgmail.com
      </li>
      <li class="contact__item">
        <svg viewBox="0 0 24 24"><circle cx="12" cy="12" r="10"/></svg>
        www.yourwebsite.com
      </li>
    </ul>
    <p class="contact__address">Your address, City<br>State, Zip 1234</p>
  </div>
</section>

</body>
</html>
```